Needs Vehicle wrap ideas. Creating a branding look for future marketing

I have a logo and need a vehicle wrap design made. The concept that is on the wrap with be applied in a similar way to all future marketing material for our company. For example once we get the wrap design made, anytime we create a postcard or flyer or business card, we'll use the same branding look. The vehicle I would like to get the design made on is a Ralton Cargomax 250 midroof. We are open to all ideas but would love to find a designer that can work off our logo and business category to come up with a great branding look. (we currently use the top right logo in the attached file)phone number is 412-593-WARM our website is BRISKHEATINGANDAIR.TEST we offer service, installation and maintenance

Target Market(s)

Heating and Cooling

Industry/Entity Type

Heating

Colors
3176b5
85acd3
0455a3
7f7f7f
5c5c5c

Requirements
Must have
• Original design, no pre-made templates. Design must have the logo (top right on attached file), phone number, website, and should list Service, Installation, and Maintenance
Should not have
• No images of people.

```html
<!DOCTYPE html>
<html lang="en">
<head>
<meta charset="utf-8">
<title>Brisk Heating &amp; Air — Vehicle Wrap</title>
<link rel="stylesheet" href="https://fonts.googleapis.com/css2?family=Exo+2:ital,wght@0,800;1,800&display=swap">
<style>
  :root {
    --navy: #0b2e86;
    --brand-blue: #3176b5;
    --light-blue: #85acd3;
    --deep-blue: #0455a3;
    --grey: #7f7f7f;
    --dark-grey: #5c5c5c;
    --red: #e41b23;
    --black: #0a0a0a;
    --white: #ffffff;
  }
  * { margin: 0; padding: 0; box-sizing: border-box; }
  html, body { width: 1200px; height: 794px; overflow: hidden; background: var(--white); }
  .wrap {
    position: relative;
    width: 1200px;
    height: 794px;
    overflow: hidden;
    font-family: "Exo 2", Arial, sans-serif;
  }
  .wrap-graphics { position: absolute; inset: 0; }

  .company-name {
    position: absolute;
    top: 190px;
    left: 70px;
    display: flex;
    align-items: center;
    gap: 22px;
    font-weight: 800;
    font-size: 68px;
    line-height: 1;
    letter-spacing: 1px;
    color: var(--navy);
    white-space: nowrap;
  }
  .company-name .name-square {
    width: 40px;
    height: 40px;
    background: var(--navy);
    flex: none;
  }

  .service-list { list-style: none; }
  .service-item {
    position: absolute;
    height: 54px;
    width: 400px;
    display: flex;
    align-items: center;
    gap: 16px;
    padding-left: 34px;
    font-style: italic;
    font-weight: 800;
    font-size: 32px;
    letter-spacing: 1px;
    color: var(--deep-blue);
  }
  .service-item svg { width: 22px; height: 30px; flex: none; }
  .service-item.service { top: 410px; left: 600px; }
  .service-item.installation { top: 480px; left: 520px; }
  .service-item.maintenance { top: 550px; left: 440px; }

  .phone {
    position: absolute;
    top: 640px;
    left: 720px;
    font-style: italic;
    font-weight: 800;
    font-size: 56px;
    line-height: 70px;
    color: var(--white);
    letter-spacing: 1px;
  }
  .phone-icon { position: absolute; top: 656px; left: 560px; width: 38px; height: 38px; }
  .website {
    position: absolute;
    top: 738px;
    left: 650px;
    font-style: italic;
    font-weight: 800;
    font-size: 30px;
    color: var(--white);
    letter-spacing: 1px;
  }
</style>
</head>
<body>
<main class="wrap">
  <svg class="wrap-graphics" viewBox="0 0 1200 794" width="1200" height="794" aria-hidden="true">
    <defs>
      <linearGradient id="silverFill" x1="0" y1="0" x2="1" y2="1">
        <stop offset="0" stop-color="#f2f2f2"/>
        <stop offset="1" stop-color="#c4c4c4"/>
      </linearGradient>
      <linearGradient id="blueFill" x1="0" y1="0" x2="1" y2="1">
        <stop offset="0" stop-color="#2a9cf0"/>
        <stop offset="1" stop-color="#1877c9"/>
      </linearGradient>
      <linearGradient id="barFill" x1="0" y1="0" x2="1" y2="0">
        <stop offset="0" stop-color="#ffffff"/>
        <stop offset="1" stop-color="#e6e6e6"/>
      </linearGradient>
    </defs>

    <rect class="panel-silver" width="1200" height="794" fill="url(#silverFill)"/>
    <polygon class="panel-blue" points="780,0 1200,0 1200,794 300,794" fill="url(#blueFill)"/>

    <polygon class="chevron-light" points="200,0 860,0 1100,300 860,560 110,560 20,330" fill="#ececec" opacity="0.85"/>
    <polygon class="chevron-edge" points="860,0 890,0 1130,300 890,560 860,560 1100,300" fill="#d6d6d6" opacity="0.9"/>

    <line class="accent-red" x1="700" y1="0" x2="1130" y2="300" stroke="var(--red)" stroke-width="3"/>
    <line class="accent-red" x1="1130" y1="300" x2="880" y2="600" stroke="var(--red)" stroke-width="3"/>
    <line class="accent-red" x1="0" y1="720" x2="330" y2="794" stroke="var(--red)" stroke-width="3"/>
    <line class="accent-white" x1="300" y1="794" x2="780" y2="0" stroke="var(--white)" stroke-width="3" opacity="0.7"/>

    <polygon class="service-bar" points="612,410 1010,410 990,464 592,464" fill="url(#barFill)"/>
    <polygon class="service-bar" points="532,480 930,480 910,534 512,534" fill="url(#barFill)"/>
    <polygon class="service-bar" points="452,550 850,550 830,604 432,604" fill="url(#barFill)"/>

    <polygon class="phone-band" points="560,640 1200,640 1200,710 540,710" fill="var(--black)"/>
    <polygon class="phone-tab" points="520,640 690,640 640,710 470,710" fill="var(--red)"/>
  </svg>

  <h1 class="company-name"><span class="name-square"></span>BRISK HEATING &amp; AIR</h1>

  <ul class="service-list">
    <li class="service-item service">
      <svg viewBox="0 0 22 30"><polygon points="0,0 10,0 22,15 10,30 0,30 12,15" fill="var(--deep-blue)"/></svg>SERVICE
    </li>
    <li class="service-item installation">
      <svg viewBox="0 0 22 30"><polygon points="0,0 10,0 22,15 10,30 0,30 12,15" fill="var(--deep-blue)"/></svg>INSTALLATION
    </li>
    <li class="service-item maintenance">
      <svg viewBox="0 0 22 30"><polygon points="0,0 10,0 22,15 10,30 0,30 12,15" fill="var(--deep-blue)"/></svg>MAINTENANCE
    </li>
  </ul>

  <svg class="phone-icon" viewBox="0 0 24 24" aria-hidden="true">
    <path fill="var(--white)" d="M6.6 10.8a15.1 15.1 0 0 0 6.6 6.6l2.2-2.2a1 1 0 0 1 1-.25 11.4 11.4 0 0 0 3.6.57 1 1 0 0 1 1 1V20a1 1 0 0 1-1 1A17 17 0 0 1 3 4a1 1 0 0 1 1-1h3.5a1 1 0 0 1 1 1c0 1.25.2 2.46.57 3.6a1 1 0 0 1-.25 1z"/>
  </svg>
  <p class="phone">412-593-WARM</p>
  <p class="website">BRISKHEATINGANDAIR.TEST</p>
</main>
</body>
</html>
```